Bright Path Attorneys Billboard Design for Personal Injury Law Firm

Need a billboard design that we can use for different versions. 1400px X 400px jpeg or png
I have attached the logo and the attorney for the billboard. Attorney Marla Benning
Here is a link to our current website brightpathlegalgroup.example

HEADLINE: HIT BY A TRUCK?
SUBHEAD: NO FEE. BIG FIGHT.
877-GRANTLY

HEADLINE: ACCIDENT?
SUBHEAD: NO FEE, UNLESS WE WIN!
877-GRANTLY

HEADLINE: BIG TRUCK. BIG CASE.
SUBHEAD: YOU PAY $0 UPFRONT
877-GRANTLY

Target Market(s)

People in Car Accident

Industry/Entity Type

Personal Injury Attorneys

```html
<!DOCTYPE html>
<html lang="en">
<head>
<meta charset="utf-8">
<title>Bright Path Attorneys – Billboard Set</title>
<link rel="stylesheet" href="https://fonts.googleapis.com/css2?family=Anton&family=Bebas+Neue&display=swap">
<style>
  :root {
    --page: #ffffff;
    --board: #000000;
    --green: #6abd45;
    --white: #ffffff;
    --logo-bar: rgba(20, 20, 20, 0.82);
  }
  * { margin: 0; padding: 0; box-sizing: border-box; }
  html, body { width: 1200px; height: 1138px; overflow: hidden; background: var(--page); }
  .canvas { position: relative; width: 1200px; height: 1138px; }

  .billboard {
    position: absolute; left: 33px; width: 1129px; height: 323px;
    background: var(--board); overflow: hidden;
  }
  .billboard--truck { top: 48px; }
  .billboard--accident { top: 417px; }
  .billboard--big-case { top: 774px; }

  .billboard__art { position: absolute; inset: 0; width: 1129px; height: 323px; }

  .rule { position: absolute; left: 0; width: 565px; height: 6px; background: var(--green); }
  .rule--top { top: 122px; }
  .rule--bottom { top: 205px; }

  .headline, .cta {
    position: absolute; font-family: "Bebas Neue", "Arial Narrow", sans-serif;
    color: var(--white); line-height: 1; white-space: nowrap;
  }
  .subhead {
    position: absolute; font-family: "Anton", "Arial Narrow", sans-serif;
    color: var(--green); line-height: 1; white-space: nowrap; letter-spacing: 1.5px;
  }

  .billboard--truck .headline { left: 54px; top: 22px; font-size: 104px; }
  .billboard--truck .subhead { left: 54px; top: 136px; font-size: 56px; }
  .billboard--truck .cta { left: 54px; top: 222px; font-size: 86px; }

  .billboard--accident .headline { left: 40px; top: 27px; font-size: 85px; }
  .billboard--accident .subhead { left: 40px; top: 139px; font-size: 50px; }
  .billboard--accident .cta { left: 40px; top: 230px; font-size: 62px; }

  .billboard--big-case .headline { left: 40px; top: 25px; font-size: 90px; }
  .billboard--big-case .subhead { left: 40px; top: 137px; font-size: 51px; }
  .billboard--big-case .cta { left: 40px; top: 227px; font-size: 72px; }

  .firm-name {
    position: absolute; left: 714px; top: 236px; width: 415px; height: 73px;
    background: var(--logo-bar); display: flex; align-items: center; gap: 14px;
    padding-left: 50px;
  }
  .firm-name__mark { width: 22px; height: 22px; background: var(--green); flex: none; }
  .firm-name__text {
    font-family: "Bebas Neue", "Arial Narrow", sans-serif; font-size: 38px;
    color: var(--white); letter-spacing: 1.5px; line-height: 1;
  }
</style>
</head>
<body>
<main class="canvas">

  <section class="billboard billboard--truck">
    <svg class="billboard__art" viewBox="0 0 1129 323" aria-hidden="false">
      <defs>
        <linearGradient id="photo-truck" x1="0" y1="0" x2="1" y2="1">
          <stop offset="0" stop-color="#5d7a2c"/>
          <stop offset="0.5" stop-color="#9a968a"/>
          <stop offset="1" stop-color="#5a5c57"/>
        </linearGradient>
      </defs>
      <polygon fill="url(#photo-truck)" points="798,0 1129,0 1129,323 711,323" role="img" aria-label="Photo: silver cab-over truck driving on a tree-lined road"/>
      <polygon fill="var(--green)" points="793,0 800,0 713,323 706,323"/>
      <polygon fill="var(--green)" points="779,0 791,0 680,323 668,323"/>
      <polygon fill="var(--green)" points="752,46 758,46 741,152 735,152"/>
    </svg>
    <div class="rule rule--top"></div>
    <div class="rule rule--bottom"></div>
    <h2 class="headline">HIT BY A TRUCK?</h2>
    <p class="subhead">NO FEE. BIG FIGHT</p>
    <p class="cta">CTA: 877-GRANTLY</p>
    <div class="firm-name"><span class="firm-name__mark"></span><span class="firm-name__text">BRIGHT PATH ATTORNEYS</span></div>
  </section>

  <section class="billboard billboard--accident">
    <svg class="billboard__art" viewBox="0 0 1129 323">
      <defs>
        <linearGradient id="photo-crash" x1="0" y1="0" x2="1" y2="1">
          <stop offset="0" stop-color="#4a5238"/>
          <stop offset="0.5" stop-color="#7d7f88"/>
          <stop offset="1" stop-color="#5a4f5c"/>
        </linearGradient>
      </defs>
      <polygon fill="url(#photo-crash)" points="798,0 1129,0 1129,323 711,323" role="img" aria-label="Photo: crumpled car rear-ended against a grey SUV after a collision"/>
      <polygon fill="var(--green)" points="793,0 800,0 713,323 706,323"/>
      <polygon fill="var(--green)" points="779,0 791,0 680,323 668,323"/>
      <polygon fill="var(--green)" points="752,46 758,46 741,152 735,152"/>
    </svg>
    <div class="rule rule--top"></div>
    <div class="rule rule--bottom"></div>
    <h2 class="headline">ACCIDENT?</h2>
    <p class="subhead">NO FEE, UNLESS WE WIN!</p>
    <p class="cta">CTA (DOMINANT): 877-GRANTLY</p>
    <div class="firm-name"><span class="firm-name__mark"></span><span class="firm-name__text">BRIGHT PATH ATTORNEYS</span></div>
  </section>

  <section class="billboard billboard--big-case">
    <svg class="billboard__art" viewBox="0 0 1129 323">
      <defs>
        <linearGradient id="photo-semi" x1="0" y1="0" x2="0.6" y2="1">
          <stop offset="0" stop-color="#3e8fa3"/>
          <stop offset="0.45" stop-color="#c98a4a"/>
          <stop offset="0.7" stop-color="#3a3e48"/>
          <stop offset="1" stop-color="#24262c"/>
        </linearGradient>
      </defs>
      <polygon fill="url(#photo-semi)" points="798,0 1129,0 1129,323 711,323" role="img" aria-label="Photo: semi truck on a highway at sunset under a teal sky"/>
      <polygon fill="var(--green)" points="793,0 800,0 713,323 706,323"/>
      <polygon fill="var(--green)" points="779,0 791,0 680,323 668,323"/>
      <polygon fill="var(--green)" points="752,46 758,46 741,152 735,152"/>
    </svg>
    <div class="rule rule--top"></div>
    <div class="rule rule--bottom"></div>
    <h2 class="headline">BIG TRUCK. BIG CASE.</h2>
    <p class="subhead">YOU PAY $0 UPFRONT</p>
    <p class="cta">CTA: 877-GRANTLY</p>
    <div class="firm-name"><span class="firm-name__mark"></span><span class="firm-name__text">BRIGHT PATH ATTORNEYS</span></div>
  </section>

</main>
</body>
</html>
```